Business Card Design

We need a business card design for our new expansion based in Bloomfield Hills, Michigan. Our company is Quiet Harbor Institute & Wellness Center. Our Academy teaches individuals of all ages and professions to live from their soul. We teach intuitive development, meditation and mindfulness; shamanic healing. And ourr healing center provides holistic services. We offer certification programs that support the ethical practices of Intuitive professionals. Our team of Intuitive Practitioners includes: doctors, psychologists, chiropractor, soul retrievers, mediums, etc who all balance their knowledge with intuitive wisdom.

We want our symbol to be the Blue Morpho Buttefly and the colors on the card to complement it. We want to communicate inspiration, healing and empowerment. Thank you
Updates

Industry/Entity Type

Business

Contact Information for Business Card

Dana Orwick
Medium. Author. Soul Retriever.
Founder, Quiet Harbor

Quiet Harbor

19 North Cedar Mill Drive Suite 100
Fernwood Heights, MI 48517
248-603-7418

www.danaorwick.example

Requirements
Must have
• blue morpho butterfly

```html
<!DOCTYPE html>
<html lang="en">
<head>
<meta charset="utf-8">
<title>Quiet Harbor — Business Card</title>
<link href="https://fonts.googleapis.com/css2?family=Arimo:wght@400;700&display=swap" rel="stylesheet">
<style>
  :root {
    --stage: #262626;
    --card-white: #ffffff;
    --ink-black: #0c0c0c;
    --panel-grey: #ececec;
    --brand-blue: #1f3ea3;
    --morpho-blue: #1e7fe0;
    --text-dark: #111111;
    --text-light: #ffffff;
  }
  * { box-sizing: border-box; margin: 0; padding: 0; }
  html, body {
    width: 1200px; height: 1000px; overflow: hidden;
    background: var(--stage);
    font-family: "Arimo", Arial, sans-serif;
  }
  .card {
    position: absolute; left: 215px;
    width: 770px; height: 440px;
    background: var(--card-white);
    overflow: hidden;
  }
  .card--front { top: 40px; }
  .card--back { top: 520px; }
  .card-shapes { position: absolute; inset: 0; }
  .brand {
    position: absolute; display: flex; flex-direction: column; align-items: center;
  }
  .brand-mark {
    width: 78px; height: 78px; border-radius: 50%;
    background: var(--morpho-blue);
    margin-bottom: 14px;
  }
  .brand-name {
    color: var(--brand-blue); font-size: 31px; font-weight: 400;
    letter-spacing: 1px; text-transform: uppercase; white-space: nowrap;
  }
  .card--front .brand { left: 335px; top: 40px; width: 330px; }
  .card--back .brand { left: 300px; top: 60px; width: 330px; }
  .person { position: absolute; left: 40px; top: 212px; color: var(--text-light); }
  .person-name { font-size: 34px; font-weight: 400; }
  .person-name strong { font-weight: 700; }
  .person-title { font-size: 19px; margin-top: 8px; }
  .contact { position: absolute; right: 20px; color: var(--text-dark); font-size: 19px; display: flex; align-items: center; gap: 16px; text-align: right; line-height: 1.35; }
  .contact--address { top: 218px; }
  .contact--phone { top: 302px; }
  .contact-icon { width: 24px; height: 24px; flex: none; }
  .website { position: absolute; left: 40px; top: 300px; color: var(--text-light); font-size: 28px; letter-spacing: 0.3px; white-space: nowrap; }
</style>
</head>
<body>

<section class="card card--front" aria-label="Business card front">
  <svg class="card-shapes" viewBox="0 0 770 440" aria-hidden="true">
    <polygon points="0,190 345,190 445,440 0,440" fill="var(--ink-black)"/>
    <polygon points="345,190 770,190 770,345 407,345" fill="var(--panel-grey)"/>
    <line x1="384" y1="285" x2="770" y2="285" stroke="#ffffff" stroke-width="3"/>
    <polygon points="413,360 770,360 770,440 445,440" fill="var(--brand-blue)"/>
  </svg>
  <div class="brand">
    <span class="brand-mark"></span>
    <span class="brand-name">Quiet Harbor</span>
  </div>
  <div class="person">
    <p class="person-name"><strong>Dana</strong> Orwick</p>
    <p class="person-title">Founder. Author. Soul Retriever</p>
  </div>
  <div class="contact contact--address">
    <p>19 North Cedar Mill Drive Suite 100<br>Fernwood Heights, MI 48517</p>
    <svg class="contact-icon" viewBox="0 0 24 24" aria-hidden="true"><path d="M12 2a7 7 0 0 0-7 7c0 5 7 13 7 13s7-8 7-13a7 7 0 0 0-7-7zm0 9.5A2.5 2.5 0 1 1 12 6.5a2.5 2.5 0 0 1 0 5z" fill="var(--text-dark)"/></svg>
  </div>
  <div class="contact contact--phone">
    <p>248-603-7418</p>
    <svg class="contact-icon" viewBox="0 0 24 24" aria-hidden="true"><path d="M3 8c0-2 3-4 9-4s9 2 9 4v2h-5V8H8v2H3z M6 12h12l2 8H4z" fill="var(--text-dark)"/><circle cx="12" cy="16" r="2" fill="#ffffff"/></svg>
  </div>
</section>

<section class="card card--back" aria-label="Business card back">
  <svg class="card-shapes" viewBox="0 0 770 440" aria-hidden="true">
    <polygon points="0,240 400,240 480,440 0,440" fill="var(--ink-black)"/>
    <polygon points="444,350 770,350 770,440 480,440" fill="var(--brand-blue)"/>
  </svg>
  <div class="brand">
    <span class="brand-mark"></span>
    <span class="brand-name">Quiet Harbor</span>
  </div>
  <p class="website">www.danaorwick.example</p>
</section>

</body>
</html>
```